Pelton|Marsh & Quillan business card contest

We need a logo for an upscale boutique diversified company involved in real estate, investments, cattle, and more. Our businesses DO NOT need to be reflected in the business card nor do we want them noted. This is our logo and colors and we love our logo and colors. Our logo looks best against a black background and we like to include the firm name in our logo usage. importantly, the names Pelton and Marsh are separated by | not / and we use an ampersand not the word and.
On the front of the card, we want to include:
company logo and name (Pelton|Marsh & Quillan)
on the back, we would definitely include:
address, email, cell #
logo and name (smaller size than front)

The variable will be location of individual name and title (mine for example is ) - whether on the front OR on the back. interested in variations from which to choose
Dr. Neil R. Whitcombe, CFA
Scientifique des Fusées Financières

we would like to use contemporary symbols for address, email address, cell # with an option for web site that we do not intend to use initially. we like two sided cards and believe this design should use four rounded corners with the standard size. we prefer thicker card stock and may look at metal.

```html
<!DOCTYPE html>
<html lang="en">
<head>
<meta charset="utf-8">
<title>Pelton|Marsh &amp; Quillan — Business Card</title>
<link rel="stylesheet" href="https://fonts.googleapis.com/css2?family=Raleway:wght@400;500&family=Open+Sans:wght@400&display=swap">
<style>
  :root {
    --stage: #23272a;
    --paper: #ffffff;
    --orange: #e07d2a;
    --orange-deep: #bd6a22;
    --ink: #5c5c5c;
    --ink-soft: #555555;
  }
  * { margin: 0; padding: 0; box-sizing: border-box; }
  html, body { width: 1200px; height: 1176px; overflow: hidden; background: var(--stage); }
  .stage { position: relative; width: 1200px; height: 1176px; }

  .card {
    position: absolute; left: 280px; width: 617px; height: 351px;
    border-radius: 20px; overflow: hidden;
    box-shadow: 0 14px 28px rgba(0,0,0,0.35);
  }
  .card--front { top: 190px; background: var(--paper); }
  .card--back {
    top: 590px;
    background: linear-gradient(225deg, var(--orange) 0%, #d07426 45%, var(--orange-deep) 100%);
  }

  .brand { position: absolute; display: flex; flex-direction: column; align-items: center; }
  .brand__mark { background: var(--ink); }
  .brand__name {
    font-family: "Raleway", sans-serif; font-weight: 500; color: var(--ink);
    white-space: nowrap; letter-spacing: 0.2px;
  }
  .card--front .brand { left: 366px; width: 218px; top: 26px; }
  .card--front .brand__mark { width: 46px; height: 46px; margin-bottom: 22px; }
  .card--front .brand__name { font-size: 19px; }
  .card--back .brand { left: 0; width: 617px; top: 82px; }
  .card--back .brand__mark { width: 64px; height: 64px; margin-bottom: 30px; }
  .card--back .brand__name { font-size: 30px; }

  .person { position: absolute; left: 31px; top: 186px; font-family: "Raleway", sans-serif; }
  .person__name { font-size: 20px; font-weight: 400; color: var(--ink); letter-spacing: 0.2px; }
  .person__name small { font-size: 15px; }
  .person__title { margin-top: 4px; font-size: 14.5px; color: var(--orange); letter-spacing: 0.1px; }

  .rule { position: absolute; left: 31px; top: 245px; width: 555px; height: 2px; background: var(--orange); }

  .contact {
    position: absolute; top: 269px; font-family: "Open Sans", sans-serif;
    font-size: 14.5px; color: var(--ink-soft); line-height: 26px;
  }
  .contact--left { left: 31px; }
  .contact--right { right: 31px; text-align: right; }
  .contact__row { display: flex; align-items: center; gap: 9px; }
  .contact__row svg { width: 13px; height: 13px; fill: var(--orange); flex: none; }

  .web-band {
    position: absolute; left: 0; bottom: 0; width: 100%; height: 26px;
    background: var(--orange); color: #fff; text-align: center;
    font-family: "Open Sans", sans-serif; font-size: 13px; letter-spacing: 2.6px; line-height: 26px;
  }
</style>
</head>
<body>
<main class="stage">
  <section class="card card--front">
    <div class="brand">
      <span class="brand__mark"></span>
      <span class="brand__name">Pelton|Marsh &amp; Quillan</span>
    </div>

    <div class="person">
      <p class="person__name">DR. NEIL R. WHITCOMBE, <small>CFA</small></p>
      <p class="person__title">SCIENTIFIQUE DES FUSÉES FINANCIÈRES</p>
    </div>

    <div class="rule"></div>

    <div class="contact contact--left">
      <p class="contact__row">
        <svg viewBox="0 0 24 24" aria-hidden="true"><path d="M7 2c1 0 1.6.6 2 1.6l1.3 3.4c.3.9 0 1.6-.7 2.1L8 10.3c1 2.3 2.9 4.4 5.3 5.6l1.3-1.5c.6-.7 1.3-.9 2.1-.6l3.4 1.4c.9.4 1.4 1 1.3 2L21 20c-.2 1.2-1.2 2-2.5 2C9.9 21.6 2.4 14 2 5.5 2 4.2 2.8 3 4 2.8z"/></svg>
        000 000 0000
      </p>
      <p class="contact__row">
        <svg viewBox="0 0 24 24" aria-hidden="true"><path d="M2 5h20v14H2z M2 5l10 8 10-8" fill="var(--orange)"/><path d="M3 6.5l9 7 9-7" fill="none" stroke="#fff" stroke-width="1.6"/></svg>
        youremail@xyz.com
      </p>
    </div>

    <div class="contact contact--right">
      <p>000, Anywehre, Somewhere</p>
      <p>City, ST 0000</p>
    </div>

    <div class="web-band">wwww.yourwebsite.com</div>
  </section>

  <section class="card card--back">
    <div class="brand">
      <span class="brand__mark"></span>
      <span class="brand__name">Pelton|Marsh &amp; Quillan</span>
    </div>
  </section>
</main>
</body>
</html>
```